New All Natural Skin Care company needs logo and label design for a new skin serum product

We need a name, logo, and label design for a new company that is producing an all in one all natural highly effective skin serum. The end result should include image imposed on clear 120z plastic bottle

We would like to see designs that promote an authentic, all natural, highly effective brand image. We need the product to standout amongst the crowded store shelves. The target customer includes Greenmarrow, Corvin Hale, and other upscale supermarket and drug store chains. This is an all in one skin product that aims to simplify a very crowded field and over cluttered market segment.

Reason: Need some great designs. Something very unique that stands out on the crowded store shelves.

Target Market(s)

men and woman, 25 years and older, who are healthy and care about their skin appearance

Industry/Entity Type

Plastic

Requirements
Nice to have
• I was inspired by a juice company called Meadowpressjuice.example Please check it out for inspiration.

I am also inspired by mrtalvik.example but am looking for more modern approach

I am interested in seeing the ingredients and benefits listed somewhere on the bottle. Here are some of them:

Jojoba Oil-moisturizing and soothing
Vitamin A-Anti Aging, Reduces wrinkles
Vitamin B-Anti Inflammatory
Vitamin C-Promote Collagen
Vitamin D3-Helps skin conditions
Vitamin E-Antioxidant
Squalene-Natural Moisturizing
Calsium Gluconate-Anti-Microbial
Acai-
Aloe-
Japanese Green Tea-anti-inflammatory
Glycerin-Moisturizing

```html
<!DOCTYPE html>
<html lang="en">
<head>
<meta charset="utf-8">
<title>VELA Face Serum: Label System</title>
<link href="https://fonts.googleapis.com/css2?family=Oswald:wght@400;500&family=Inter:wght@300;400;600&display=swap" rel="stylesheet">
<style>
  :root {
    --teal-deep: #0b443f;
    --teal: #155e57;
    --teal-light: #2a7a71;
    --wood: #4a2a1c;
    --wood-light: #7a4a32;
    --ink: #1f1f1f;
    --label-red: #8a2a1a;
    --line-grey: #b9bec0;
    --paper: #ffffff;
    --jar-glass: #eef1f2;
    --display: "Oswald", "Arial Narrow", sans-serif;
    --body: "Inter", "Helvetica Neue", Arial, sans-serif;
  }
  * { margin: 0; padding: 0; box-sizing: border-box; }
  html, body { width: 988px; height: 1200px; overflow: hidden; background: var(--paper); }
  .sheet { position: relative; width: 988px; height: 1200px; font-family: var(--body); color: var(--ink); }
  .abs { position: absolute; }

  .tag { position: absolute; font-family: var(--body); font-weight: 600; font-size: 7px; letter-spacing: .5px; color: var(--label-red); text-transform: uppercase; }
  .tag--large { font-size: 11px; }

  .type-spec { font-family: var(--display); font-size: 16px; color: var(--ink); }
  .type-spec--light { font-family: var(--body); font-weight: 300; font-size: 15px; }
  .type-spec::before { content: ""; display: inline-block; width: 16px; height: 1px; background: var(--label-red); vertical-align: middle; margin-right: 5px; }

  .mini-logo { position: absolute; top: 404px; font-family: var(--display); font-weight: 500; font-size: 14px; }

  .front-panel { left: 116px; top: 516px; width: 320px; height: 306px;
    background: linear-gradient(135deg, var(--teal-deep) 0%, var(--teal-light) 50%, var(--teal-deep) 100%);
    color: #fff; text-align: center; }
  .front-name { position: absolute; left: 0; right: 0; top: 70px; font-family: var(--display); font-weight: 500; font-size: 100px; line-height: 1; letter-spacing: 1px; }
  .front-sub { position: absolute; left: 0; right: 0; top: 196px; font-size: 15px; font-weight: 300; }
  .front-size { position: absolute; left: 0; right: 0; top: 250px; font-size: 17px; font-weight: 300; letter-spacing: 1px; }

  .back-panel { left: 161px; top: 862px; width: 225px; height: 263px;
    background: linear-gradient(160deg, var(--teal-deep) 0%, var(--teal-light) 45%, var(--teal-deep) 100%); color: #fff; padding: 14px; }
  .back-intro { font-size: 10.5px; line-height: 1.25; text-align: center; margin: 0 6px 12px; }
  .back-heading { font-family: var(--display); font-weight: 400; font-size: 12px; letter-spacing: 1px; text-align: center; margin-bottom: 7px; }
  .benefits { display: grid; grid-template-columns: 1fr 1fr; column-gap: 10px; }
  .benefit { margin-bottom: 5px; line-height: 1.05; }
  .benefit b { display: block; font-family: var(--display); font-weight: 400; font-size: 10.5px; }
  .benefit span { display: block; font-size: 7.5px; font-weight: 300; padding-left: 8px; }

  .lockup { position: absolute; left: 647px; width: 337px; text-align: center;
    font-family: var(--display); font-weight: 500; font-size: 88px; line-height: 1; color: var(--teal); }
</style>
</head>
<body>
<main class="sheet">

  <svg width="0" height="0" style="position:absolute">
    <defs>
      <linearGradient id="wood" x1="0" x2="1"><stop offset="0" stop-color="#4a2a1c"/><stop offset=".5" stop-color="#7a4a32"/><stop offset="1" stop-color="#4a2a1c"/></linearGradient>
      <linearGradient id="tealG" x1="0" y1="0" x2="1" y2="1"><stop offset="0" stop-color="#0b443f"/><stop offset=".5" stop-color="#2a7a71"/><stop offset="1" stop-color="#0b443f"/></linearGradient>
    </defs>
  </svg>

  <!-- Style guide -->
  <p class="tag" style="left:41px; top:184px;">Typeface</p>
  <p class="abs type-spec" style="left:100px; top:180px;">Corsa Condensed</p>
  <p class="abs type-spec type-spec--light" style="left:100px; top:204px;">Lindell Light</p>

  <p class="tag" style="left:41px; top:236px;">Color Palette</p>
  <svg class="abs" style="left:66px; top:248px;" width="150" height="118" viewBox="0 0 150 118" role="img" aria-label="Colour palette swatches: walnut wood, deep teal, patterned teal">
    <rect x="10" y="0" width="56" height="54" fill="url(#wood)"/>
    <rect x="78" y="32" width="56" height="54" fill="url(#tealG)"/>
    <rect x="10" y="64" width="56" height="54" fill="var(--teal)"/>
  </svg>

  <p class="tag" style="left:41px; top:384px;">Logo</p>
  <p class="mini-logo" style="left:42px; color:var(--teal);">VELA</p>
  <p class="mini-logo" style="left:92px; color:var(--line-grey);">VELA</p>
  <p class="mini-logo" style="left:142px; color:var(--teal-light);">VELA</p>
  <p class="mini-logo" style="left:192px; color:var(--wood);">VELA</p>

  <!-- Thumbnail panels -->
  <p class="tag" style="left:249px; top:170px;">Font Panel</p>
  <svg class="abs" style="left:249px; top:180px;" width="90" height="84" viewBox="0 0 90 84">
    <rect width="90" height="84" fill="url(#tealG)"/>
    <text x="45" y="44" text-anchor="middle" font-family="Oswald, sans-serif" font-weight="500" font-size="24" fill="#fff">VELA</text>
    <text x="45" y="58" text-anchor="middle" font-family="Inter, sans-serif" font-size="4.5" fill="#fff">All Natural Face Serum</text>
    <text x="45" y="72" text-anchor="middle" font-family="Inter, sans-serif" font-size="5" fill="#fff">12 OZ</text>
  </svg>

  <p class="tag" style="left:356px; top:164px;">Back Panel</p>
  <svg class="abs" style="left:356px; top:174px;" width="88" height="104" viewBox="0 0 88 104">
    <rect width="88" height="104" fill="url(#tealG)"/>
    <g font-family="Inter, sans-serif" fill="#fff" text-anchor="middle">
      <text x="44" y="14" font-size="5">Natural serum for daily care</text>
      <text x="44" y="30" font-size="6" font-family="Oswald, sans-serif">BENEFITS</text>
      <text x="44" y="44" font-size="4.5">Jojoba Oil · Squalene</text>
      <text x="44" y="54" font-size="4.5">Vitamin A · Glycerin</text>
      <text x="44" y="64" font-size="4.5">Vitamin C · Aloe</text>
    </g>
  </svg>

  <!-- Jars, flat -->
  <svg class="abs" style="left:244px; top:281px;" width="104" height="152" viewBox="0 0 104 152" role="img" aria-label="Serum jar, front label">
    <rect x="6" y="0" width="92" height="26" rx="4" fill="url(#wood)"/>
    <rect x="2" y="26" width="100" height="124" rx="6" fill="var(--jar-glass)" stroke="#d3d8da"/>
    <rect x="20" y="46" width="64" height="52" fill="url(#tealG)"/>
    <text x="52" y="77" text-anchor="middle" font-family="Oswald, sans-serif" font-weight="500" font-size="20" fill="#fff">VELA</text>
    <text x="52" y="89" text-anchor="middle" font-family="Inter, sans-serif" font-size="5" fill="#fff">Face Serum</text>
  </svg>
  <svg class="abs" style="left:375px; top:281px;" width="116" height="152" viewBox="0 0 116 152" role="img" aria-label="Serum jar, back label">
    <rect x="6" y="0" width="104" height="26" rx="4" fill="url(#wood)"/>
    <rect x="2" y="26" width="112" height="124" rx="6" fill="var(--jar-glass)" stroke="#d3d8da"/>
    <rect x="10" y="40" width="96" height="92" fill="url(#tealG)"/>
    <g font-family="Inter, sans-serif" fill="#fff" text-anchor="middle" font-size="5">
      <text x="58" y="56">Natural serum for daily care</text>
      <text x="58" y="76">Jojoba Oil</text>
      <text x="58" y="88">Vitamin E</text>
      <text x="58" y="100">Aloe</text>
    </g>
  </svg>

  <!-- Front panel -->
  <p class="tag tag--large" style="left:131px; top:491px;">Font Panel</p>
  <section class="abs front-panel">
    <p class="front-name">VELA</p>
    <p class="front-sub">All Natural Face Serum</p>
    <p class="front-size">12 OZ</p>
  </section>

  <!-- Back panel -->
  <p class="tag tag--large" style="left:161px; top:842px;">Back Panel</p>
  <section class="abs back-panel">
    <p class="back-intro">Our all natural serum transforms your skin by using ingredients that are scientifically proven to moisturize &amp; revitalize your skin's natural beauty.</p>
    <h2 class="back-heading">VELA BENEFITS</h2>
    <div class="benefits">
      <div>
        <p class="benefit"><b>Jojoba Oil</b><span>Moisturizing, Soothing</span></p>
        <p class="benefit"><b>Vitamin A</b><span>Anti Aging &amp; Reduces Wrinkles</span></p>
        <p class="benefit"><b>Vitamin B</b><span>Anti Inflammatory</span></p>
        <p class="benefit"><b>Vitamin C-Promote</b><span>Collagen</span></p>
        <p class="benefit"><b>Vitamin D3</b><span>Helps skin condition</span></p>
        <p class="benefit"><b>Vitamin E</b><span>Antioxidant</span></p>
      </div>
      <div>
        <p class="benefit"><b>Squalene</b><span>Natural Moisturizing</span></p>
        <p class="benefit"><b>Calcium Gluconate</b><span>Anti-Microbial</span></p>
        <p class="benefit"><b>Japanese Green Tea</b><span>Anti-Inflammatory</span></p>
        <p class="benefit"><b>Glycerin</b><span>Moisturizing</span></p>
        <p class="benefit"><b>Acai</b></p>
        <p class="benefit"><b>Aloe</b></p>
      </div>
    </div>
  </section>

  <!-- Name lockups -->
  <p class="lockup" style="top:262px;">VELA</p>
  <p class="lockup" style="top:618px;">VELA</p>
  <p class="lockup" style="top:985px;">VELA</p>

</main>
</body>
</html>
```